Brisk Hollow Builders Needs A Flyer

We need a flyer for our newest product "The Cedarlane Garden Workroom"

Here is some copy for the flyer:

1. More and more people everyday are working from home and finding it difficult to disconnect from home activities in order to focus on their work. They are also finding it very expensive to add on to their existing house for a quiet place. Our archatectually stunning, Cedarlane Garden Workroom is the answer. The office studio measures 16' wide and 10' deep. 160 Square feet of space.

Perfect for dozens of purposes. Home office, design studio, artist studio, home school office, reading room, craft studio, drafting room.

Features include:

- Steel Framing. 40-60% lighter then wood, higher strength to weight ratio, resistant to mold and fire and steel is the most recycled material on earth!
- Spray foam insulation. Cool in the summer and warm in the winter.
- HVAC Mini Split with wireless remote control and thermostat.
- 100% Off grid with enough solar and battery storage to run your entire office. No need to pay for an expensive electric installation.
- Flush fitting floor outlets to reduce wires.
- TV mount (Optional with pre-wired electric, HDMI, digital audio & Cat 6)
- Windows are tempered glass custom made by Morvik Glazing.
- Solar qualifies for a 26% tax credit. This is not a write-off rather it is a direct reduction on your tax obligation.
- Thousands of dollars less than adding onto your home.
- Custom color, siding, features available.

This beautiful back yard office is delivered 100% assembled and ready to enjoy on the day of delivery.

We ship nationwide from our factory in South Carolina. Give us a call anytime to speak to a designer and start your dream office today!

555-318-4027
info@BriskHollowBuilders.example

```html
<!DOCTYPE html>
<html lang="en">
<head>
<meta charset="utf-8">
<title>Brisk Hollow Builders – Cedarlane Garden Workroom Flyer</title>
<link href="https://fonts.googleapis.com/css2?family=Barlow+Condensed:wght@600;700&family=Inter:wght@400;600;700&family=Roboto:wght@700&display=swap" rel="stylesheet">
<style>
  :root{
    --stage:#8f8f8f;
    --paper:#ffffff;
    --green:#3f8a2c;
    --green-dark:#0f4a12;
    --green-light:#5aa63f;
    --orange:#e69a1c;
    --orange-deep:#e0901a;
    --ink:#2b2b2b;
    --sky:#b9cfe0;
    --foliage:#6b8a4e;
  }
  *{margin:0;padding:0;box-sizing:border-box}
  html,body{width:1200px;height:851px;overflow:hidden}
  body{background:var(--stage);font-family:"Inter",Arial,sans-serif;color:var(--ink);position:relative}
  .page{position:absolute;top:108px;width:452px;height:639px;background:var(--paper);overflow:hidden;box-shadow:0 10px 18px rgba(0,0,0,.25)}
  .page--front{left:129px}
  .page--back{left:636px}
  .page svg.bands{position:absolute;inset:0}
  .abs{position:absolute}
  .intro{left:32px;top:29px;width:400px;font-size:9.6px;line-height:1.26}
  .headline{left:30px;top:80px;font-family:"Barlow Condensed",Arial Narrow,sans-serif;font-weight:700;font-size:17.5px;line-height:1;text-transform:uppercase;letter-spacing:.2px}
  .headline .o{color:var(--orange)}
  .headline .g{color:var(--green)}
  .size{left:30px;top:141px;font-size:9.6px;line-height:1.28}
  .brand{font-family:"Barlow Condensed",Arial Narrow,sans-serif;font-weight:700;color:var(--orange);text-transform:uppercase;display:flex;align-items:center;gap:6px;line-height:1}
  .brand .dot{width:14px;height:14px;border-radius:50%;background:var(--green);flex:none}
  .brand--front{left:275px;top:130px;font-size:22px;width:160px}
  .brand--back{left:230px;top:335px;font-size:24px;width:190px}
  .purposes{left:260px;top:429px;width:145px;height:137px;border-radius:8px;background:linear-gradient(160deg,var(--green-light),var(--green-dark));padding:13px 0 0 17px;box-shadow:0 4px 5px rgba(0,0,0,.25)}
  .purposes h3{font-family:"Barlow Condensed",Arial Narrow,sans-serif;font-weight:600;color:var(--orange);font-size:12.5px;line-height:1.1;text-transform:uppercase;margin-bottom:7px}
  .purposes ul{list-style:none}
  .purposes li{color:#fff;font-size:8.6px;font-weight:600;line-height:11px;display:flex;align-items:center;gap:4px}
  .tick{width:8px;height:8px;flex:none}
  .contact-front{left:260px;top:575px}
  .phone{font-family:"Roboto",Arial,sans-serif;font-weight:700;color:var(--green);font-size:17px;display:flex;align-items:center;gap:3px}
  .contact-front p{font-size:9.6px;line-height:1.22}
  .feat-tag{left:30px;top:19px;height:22px;padding:0 16px 0 10px;background:var(--orange);border-radius:11px 0 0 11px;clip-path:polygon(0 0,88% 0,100% 100%,0 100%);font-family:"Barlow Condensed",Arial Narrow,sans-serif;font-weight:700;font-size:18px;line-height:22px;color:var(--green-dark);text-transform:uppercase}
  .feat-rule{left:190px;top:40px;width:234px;height:1px;background:var(--orange)}
  .features{left:32px;top:52px;width:400px;list-style:none}
  .features li{color:#fff;font-size:9.6px;line-height:12px;display:flex;gap:8px;margin-bottom:6px}
  .features .tick{width:10px;height:10px;margin-top:1px}
  .delivery{left:32px;top:323px;width:190px;font-size:9.6px;line-height:1.26}
  .delivery p{margin-bottom:7px}
  .delivery b{color:var(--green);font-weight:700}
  .product{left:87px;top:409px;width:271px;height:140px;background:linear-gradient(180deg,#2f3130 0 7%,#cfc8bf 7% 100%)}
  .cta{left:20px;top:543px;width:410px;height:73px;border-radius:12px;background:linear-gradient(90deg,var(--orange),var(--orange-deep));display:flex;align-items:center;box-shadow:0 5px 6px rgba(0,0,0,.2)}
  .cta-call{width:212px;text-align:right;padding-right:6px;font-family:"Barlow Condensed",Arial Narrow,sans-serif;font-weight:700;color:#fff;font-size:14px;line-height:15.5px;text-transform:uppercase;border-right:1px solid rgba(255,255,255,.7)}
  .cta-info{padding-left:6px;color:#fff}
  .cta-info .num{font-family:"Roboto",Arial,sans-serif;font-weight:700;font-size:22px;line-height:1}
  .cta-info p{font-size:9.9px;line-height:1.3}
</style>
</head>
<body>

<section class="page page--front">
  <svg class="bands" viewBox="0 0 452 639" width="452" height="639">
    <polygon points="0,252 148,198 452,250 452,278 148,208 0,262" fill="var(--green)"/>
    <polygon points="0,262 148,208 452,278 452,440 148,428 0,464" fill="url(#frontPhoto)" role="img" aria-label="Photo of the garden workroom studio in a landscaped back yard"/>
    <polygon points="0,464 148,428 452,440 452,468 148,448 0,493" fill="var(--orange)"/>
    <rect x="0" y="487" width="216" height="152" fill="url(#roofPhoto)" role="img" aria-label="Close-up photo of the studio roof with solar panels"/>
    <defs>
      <linearGradient id="frontPhoto" x1="0" y1="0" x2="0" y2="1">
        <stop offset="0" stop-color="var(--sky)"/>
        <stop offset=".35" stop-color="#7f9a6a"/>
        <stop offset="1" stop-color="var(--foliage)"/>
      </linearGradient>
      <linearGradient id="roofPhoto" x1="0" y1="0" x2="0" y2="1">
        <stop offset="0" stop-color="#8aa0b8"/>
        <stop offset=".3" stop-color="#5d6266"/>
        <stop offset="1" stop-color="#4a4c4d"/>
      </linearGradient>
    </defs>
  </svg>

  <p class="abs intro">More and more people everyday are working from home &amp; finding it difficult to disconnect from home activities in order to focus on their work. They are also finding it very expensive to add on to their existing house for a quiet place.</p>

  <h1 class="abs headline"><span class="o">Our architectually stunning</span><br><span class="g">Cedarlane Garden Workroom</span><br><span class="g">is the answer.</span></h1>

  <p class="abs size">The office studio<br>measures <b>16'</b> wide &amp; <b>10'</b> deep.<br><b>160</b> Square feet of space.</p>

  <div class="abs brand brand--front"><span class="dot"></span><span>Brisk Hollow Builders</span></div>

  <div class="abs purposes">
    <h3>Perfect for<br>dozens of purposes.</h3>
    <ul>
      <li><svg class="tick" viewBox="0 0 10 10"><circle cx="5" cy="5" r="5" fill="var(--orange)"/><path d="M2.8 5.2l1.6 1.6 3-3.4" stroke="#fff" stroke-width="1.4" fill="none"/></svg>Home office</li>
      <li><svg class="tick" viewBox="0 0 10 10"><circle cx="5" cy="5" r="5" fill="var(--orange)"/><path d="M2.8 5.2l1.6 1.6 3-3.4" stroke="#fff" stroke-width="1.4" fill="none"/></svg>Design studio</li>
      <li><svg class="tick" viewBox="0 0 10 10"><circle cx="5" cy="5" r="5" fill="var(--orange)"/><path d="M2.8 5.2l1.6 1.6 3-3.4" stroke="#fff" stroke-width="1.4" fill="none"/></svg>Artist studio</li>
      <li><svg class="tick" viewBox="0 0 10 10"><circle cx="5" cy="5" r="5" fill="var(--orange)"/><path d="M2.8 5.2l1.6 1.6 3-3.4" stroke="#fff" stroke-width="1.4" fill="none"/></svg>Home school office</li>
      <li><svg class="tick" viewBox="0 0 10 10"><circle cx="5" cy="5" r="5" fill="var(--orange)"/><path d="M2.8 5.2l1.6 1.6 3-3.4" stroke="#fff" stroke-width="1.4" fill="none"/></svg>Reading room</li>
      <li><svg class="tick" viewBox="0 0 10 10"><circle cx="5" cy="5" r="5" fill="var(--orange)"/><path d="M2.8 5.2l1.6 1.6 3-3.4" stroke="#fff" stroke-width="1.4" fill="none"/></svg>Craft studio</li>
      <li><svg class="tick" viewBox="0 0 10 10"><circle cx="5" cy="5" r="5" fill="var(--orange)"/><path d="M2.8 5.2l1.6 1.6 3-3.4" stroke="#fff" stroke-width="1.4" fill="none"/></svg>Drafting room</li>
    </ul>
  </div>

  <div class="abs contact-front">
    <div class="phone"><svg width="13" height="13" viewBox="0 0 24 24"><path d="M6.6 10.8a15.1 15.1 0 0 0 6.6 6.6l2.2-2.2a1 1 0 0 1 1-.25 11.4 11.4 0 0 0 3.6.57 1 1 0 0 1 1 1V20a1 1 0 0 1-1 1A17 17 0 0 1 3 4a1 1 0 0 1 1-1h3.5a1 1 0 0 1 1 1c0 1.25.2 2.45.57 3.57a1 1 0 0 1-.25 1z" fill="var(--green)"/></svg>555-318-4027</div>
    <p>info@BriskHollowBuilders.example</p>
    <p>www.BriskHollowBuilders.example</p>
  </div>
</section>

<section class="page page--back">
  <svg class="bands" viewBox="0 0 452 639" width="452" height="639">
    <defs>
      <linearGradient id="greenField" x1="0" y1="0" x2="1" y2="0">
        <stop offset="0" stop-color="var(--green-dark)"/>
        <stop offset="1" stop-color="var(--green-light)"/>
      </linearGradient>
    </defs>
    <polygon points="0,0 452,0 452,300 307,263 124,289 0,262" fill="url(#greenField)"/>
    <polygon points="0,262 124,289 307,263 452,300 452,322 307,286 124,315 0,292" fill="var(--orange)"/>
  </svg>

  <div class="abs feat-tag">Features include:</div>
  <div class="abs feat-rule"></div>

  <ul class="abs features">
    <li><svg class="tick" viewBox="0 0 10 10"><circle cx="5" cy="5" r="5" fill="var(--orange)"/><path d="M2.8 5.2l1.6 1.6 3-3.4" stroke="#fff" stroke-width="1.4" fill="none"/></svg><span>Steel Framing. 40-60% lighter then wood, higher strength to weight ratio, resistant to mold and fire and steel is the most recycled material on earth!</span></li>
    <li><svg class="tick" viewBox="0 0 10 10"><circle cx="5" cy="5" r="5" fill="var(--orange)"/><path d="M2.8 5.2l1.6 1.6 3-3.4" stroke="#fff" stroke-width="1.4" fill="none"/></svg><span>Spray foam insulation. Cool in the summer and warm in the winter.</span></li>
    <li><svg class="tick" viewBox="0 0 10 10"><circle cx="5" cy="5" r="5" fill="var(--orange)"/><path d="M2.8 5.2l1.6 1.6 3-3.4" stroke="#fff" stroke-width="1.4" fill="none"/></svg><span>HVAC Mini Split with wireless remote control and thermostat.</span></li>
    <li><svg class="tick" viewBox="0 0 10 10"><circle cx="5" cy="5" r="5" fill="var(--orange)"/><path d="M2.8 5.2l1.6 1.6 3-3.4" stroke="#fff" stroke-width="1.4" fill="none"/></svg><span>100% Off grid with enough solar and battery storage to run your entire office. No need to pay for an expensive electric installation.</span></li>
    <li><svg class="tick" viewBox="0 0 10 10"><circle cx="5" cy="5" r="5" fill="var(--orange)"/><path d="M2.8 5.2l1.6 1.6 3-3.4" stroke="#fff" stroke-width="1.4" fill="none"/></svg><span>Flush fitting floor outlets to reduce wires.</span></li>
    <li><svg class="tick" viewBox="0 0 10 10"><circle cx="5" cy="5" r="5" fill="var(--orange)"/><path d="M2.8 5.2l1.6 1.6 3-3.4" stroke="#fff" stroke-width="1.4" fill="none"/></svg><span>TV mount (Optional with pre-wired electric, HDMI, digital audio &amp; Cat 6)</span></li>
    <li><svg class="tick" viewBox="0 0 10 10"><circle cx="5" cy="5" r="5" fill="var(--orange)"/><path d="M2.8 5.2l1.6 1.6 3-3.4" stroke="#fff" stroke-width="1.4" fill="none"/></svg><span>Windows are tempered glass custom made by Morvik Glazing.</span></li>
    <li><svg class="tick" viewBox="0 0 10 10"><circle cx="5" cy="5" r="5" fill="var(--orange)"/><path d="M2.8 5.2l1.6 1.6 3-3.4" stroke="#fff" stroke-width="1.4" fill="none"/></svg><span>Solar qualifies for a 26% tax credit. This is not a write-off rather it is a direct reduction on your tax obligation.</span></li>
    <li><svg class="tick" viewBox="0 0 10 10"><circle cx="5" cy="5" r="5" fill="var(--orange)"/><path d="M2.8 5.2l1.6 1.6 3-3.4" stroke="#fff" stroke-width="1.4" fill="none"/></svg><span>Thousands of dollars less than adding onto your home.</span></li>
    <li><svg class="tick" viewBox="0 0 10 10"><circle cx="5" cy="5" r="5" fill="var(--orange)"/><path d="M2.8 5.2l1.6 1.6 3-3.4" stroke="#fff" stroke-width="1.4" fill="none"/></svg><span>Custom color, siding, features available.</span></li>
  </ul>

  <div class="abs delivery">
    <p>This beautiful back yard office is delivered <b>100% assembled</b> &amp; ready to enjoy on the day of delivery.</p>
    <p>We ship nationwide from our factory in <b>South Carolina.</b></p>
  </div>

  <div class="abs brand brand--back"><span class="dot"></span><span>Brisk Hollow Builders</span></div>

  <div class="abs product" role="img" aria-label="Front view photo of the garden workroom with glass doors and furnished interior"></div>

  <div class="abs cta">
    <div class="cta-call">Give us a call any time<br>to speak to a designer &amp; start<br>your dream office today!</div>
    <div class="cta-info">
      <div class="num">555-318-4027</div>
      <p>info@BriskHollowBuilders.example</p>
      <p>www.BriskHollowBuilders.example</p>
    </div>
  </div>
</section>

</body>
</html>
```